Icon Design Project

I need icons for 3 parts of the the business which we are now going to be focusing on. Icons need to be very basic vectors, without too many layers, describing the 3 keywords. They should be black and sit inside an orange circle. The keywords, in order, from left to right are:
DESIGN
RENOVATE
STYLE

Note: these keywords relate to the services of Home Renovations that the company this is fore represents. We do home transformations, where customers come into our showroom, tell us they need a make-over for their kitchen, bathroom, bedroom, living room or whatever, and then they tell us how they want it changed, which we design on the computer. Proceeding that, we send in our builders and start the physical renovation job. And then the last step is styling, which is where help choose suitable furniture and items for the house which we put into place for them to suit the look they desire.

Make sure you place 3 icons in a row in order of Design Renovate Style so I can compare accordingly.

UPDATE: In terms of sizing, they should be able to appear on a business card and be visible, but just know they will also be used on DL sized brochures. So, I hope that helps.

UPDATE 2: I've attached the best design so far. I require something like that, but in a modern look. So a simple layer vector without so much detail.

1. human with a book or computer
2. a modern house coming out of a box
3. a modern sofa, thats easily identifiable

Reason: We haven't received exactly what we want as yet, so am extending this by a day. Please submit more designs.

Hi all.

I have included an image in the brief files of what the best design was so far.
I want something like that, but in 1 colour, and modern looking.
Have a read of these notes.

Loma

Target Market(s)

35 to 60 year old male and female homeowners of high socio-economic status

Industry/Entity Type

House

Requirements
Must have
• Black icons placed in an orange filled circle
Nice to have
• A bit of 3D/glass effect on each icon
Should not have
• Too many layers. Should be simple detailed enough to see the item, but not too complicated where it has multiple layers and borders and outlines.

```html
<!DOCTYPE html>
<html lang="en">
<head>
<meta charset="utf-8">
<title>Design · Renovate · Style</title>
<link rel="stylesheet" href="https://fonts.googleapis.com/css2?family=Comfortaa:wght@700&display=swap">
<style>
  :root {
    --bg-light: #9a9a9a;
    --bg-mid: #5c5c5c;
    --bg-dark: #2b2b2b;
    --orange-light: #ffb347;
    --orange: #f28c1e;
    --orange-deep: #d96a0a;
    --well: #474747;
    --icon-light: #f2f2f2;
    --icon-shade: #b5b5b5;
    --label: #ffffff;
  }
  html, body {
    margin: 0;
    padding: 0;
    overflow: hidden;
  }
  .canvas {
    position: relative;
    width: 1200px;
    height: 841px;
    overflow: hidden;
    background: radial-gradient(ellipse 70% 75% at 45% 50%, var(--bg-light) 0%, var(--bg-mid) 45%, var(--bg-dark) 100%);
  }
  .defs {
    position: absolute;
    width: 0;
    height: 0;
  }
  .service {
    position: absolute;
    top: 327px;
    width: 300px;
    text-align: center;
  }
  .service--design { left: 94px; }
  .service--renovate { left: 468px; }
  .service--style { left: 842px; }
  .service__badge {
    display: block;
    width: 250px;
    height: 250px;
    margin: 0 auto;
    overflow: visible;
  }
  .service__label {
    margin: 22px 0 0;
    font-family: "Comfortaa", sans-serif;
    font-weight: 700;
    font-size: 60px;
    line-height: 1.1;
    letter-spacing: 1px;
    white-space: nowrap;
    color: var(--label);
  }
  .service--design .service__label { margin-left: 20px; }
  .service--renovate .service__label { margin-left: 52px; }
  .service--style .service__label { margin-left: -16px; }
</style>
</head>
<body>
<main class="canvas">
  <svg class="defs" aria-hidden="true">
    <defs>
      <linearGradient id="ring-fill" x1="0" y1="0" x2="0" y2="1">
        <stop offset="0" stop-color="var(--orange-light)"/>
        <stop offset="0.55" stop-color="var(--orange)"/>
        <stop offset="1" stop-color="var(--orange-deep)"/>
      </linearGradient>
      <radialGradient id="drop-shadow" cx="0.5" cy="0.5" r="0.5">
        <stop offset="0" stop-color="#000" stop-opacity="0.55"/>
        <stop offset="1" stop-color="#000" stop-opacity="0"/>
      </radialGradient>
      <linearGradient id="icon-fill" x1="0" y1="0" x2="1" y2="1">
        <stop offset="0" stop-color="var(--icon-light)"/>
        <stop offset="1" stop-color="var(--icon-shade)"/>
      </linearGradient>
      <g id="ring">
        <ellipse cx="0" cy="104" rx="112" ry="22" fill="url(#drop-shadow)"/>
        <circle r="118" fill="url(#ring-fill)"/>
        <path d="M-112 -36 A118 118 0 0 1 112 -36 A125 80 0 0 0 -112 -36 Z" fill="#fff" opacity="0.22"/>
        <path d="M-114 24 A118 118 0 0 0 114 24 A135 68 0 0 1 -114 24 Z" fill="#fff" opacity="0.12"/>
        <circle r="82" fill="var(--well)"/>
      </g>
    </defs>
  </svg>

  <section class="service service--design">
    <svg class="service__badge" viewBox="-125 -125 250 250" role="img" aria-label="Pencil icon for design">
      <use href="#ring"/>
      <g transform="scale(1.1) rotate(30)">
        <rect x="-13" y="-44" width="26" height="60" rx="3" fill="url(#icon-fill)"/>
        <ellipse cx="0" cy="-44" rx="13" ry="5" fill="var(--icon-light)"/>
        <path d="M-13 16 L0 44 L13 16 Z" fill="var(--icon-shade)"/>
        <path d="M-4 36 L0 44 L4 36 Z" fill="var(--well)"/>
      </g>
    </svg>
    <p class="service__label">Design</p>
  </section>

  <section class="service service--renovate">
    <svg class="service__badge" viewBox="-125 -125 250 250" role="img" aria-label="Hard hat icon for renovate">
      <use href="#ring"/>
      <g transform="scale(1.1)">
        <path d="M-42 12 C-42 -22 -20 -38 6 -38 C32 -38 46 -18 46 12 Z" fill="url(#icon-fill)"/>
        <path d="M2 -38 C8 -24 10 -8 10 12 L16 12 C16 -8 14 -26 8 -38 Z" fill="var(--icon-shade)"/>
        <path d="M-54 12 L50 12 C52 18 48 24 40 24 L-48 24 C-56 24 -58 16 -54 12 Z" fill="var(--icon-light)"/>
      </g>
    </svg>
    <p class="service__label">Renovate</p>
  </section>

  <section class="service service--style">
    <svg class="service__badge" viewBox="-125 -125 250 250" role="img" aria-label="Paint can icon for style">
      <use href="#ring"/>
      <g transform="scale(1.1)">
        <path d="M-28 -34 L28 -34 L26 36 C26 42 -26 42 -26 36 Z" fill="url(#icon-fill)"/>
        <ellipse cx="0" cy="-34" rx="28" ry="7" fill="var(--icon-light)"/>
        <ellipse cx="0" cy="-34" rx="22" ry="4" fill="var(--icon-shade)"/>
        <path d="M-28 -30 C-20 -24 -12 -22 -12 -8 L-12 30 C-12 36 -20 36 -20 30 L-20 -10 C-22 -18 -26 -20 -28 -22 Z" fill="var(--icon-shade)"/>
        <rect x="-46" y="8" width="14" height="30" rx="3" fill="var(--icon-shade)"/>
        <rect x="-43" y="-10" width="8" height="20" fill="var(--icon-light)"/>
      </g>
    </svg>
    <p class="service__label">Style</p>
  </section>
</main>
</body>
</html>
```